Poster design for the stage play Meet Me at the Corner Drugstore, Rusty Calhoun, Rusty Calhoun

I need a poster designed for an upcoming stage play titled, Meet Me at the Corner Drugstore, Rusty Calhoun, Rusty Calhoun.

Play synopsis: In a small town dime store in West Texas, the "Devotees of Rusty Calhoun" gather for their twentieth reunion. Now middle-aged women, they were teenagers when Calhoun filmed Dustline two decades ago in nearby Marfa. One of them, an extra in the film, has a child whom she says was conceived with Calhoun during the shoot. The ladies' congenial reminiscences mingle with flash backs to their youth; then the arrival of a stunning but familiar stranger sets off a series of confrontations that smash their delusions and expose bitter disappointments.

The poster must have the following information:

Title in larger font: Meet Me at the Corner Drugstore, Rusty Calhoun, Rusty Calhoun
Playwright in a medium font: by Al Moravec
Director in a slightly smaller font: directed by Roy Pettibone

I have attached a couple examples of poster designs used by other companies that I like. One sets the mood of rural Texas with a silhouette of Rusty Calhoun from the movie, Dustline, including a 1950s automobile from the era when Dustline was filmed. The other uses a clip of the artwork/graphics used to promote Dustline.

This play was made into a movie in 1982. If you do a search on Meet Me…Rusty Calhoun posters you will see a lot of the photos and posters used to promote the movie. The stage play poster should not have the look or sentiment of the movie poster in any way.

Target Market(s)

Theatre and arts supporters

Industry/Entity Type

Town

Requirements
Must have
• The poster must have the following information:
• Title in larger font: Meet Me at the Corner Drugstore, Rusty Calhoun, Rusty Calhoun
• Playwright in a medium font: by Al Moravec
• Director in a slightly smaller font: directed by Roy Pettibone
Nice to have
• I have attached a couple examples of poster designs used by other companies that I like. One sets the mood of rural Texas with a silhouette of Rusty Calhoun from the movie, Dustline, including a 1950s automobile from the era when Dustline was filmed. The other uses a clip of the artwork/graphics used to promote Dustline.
Should not have
• This play was made into a movie in 1982. If you do a search on Meet Me…Rusty Calhoun posters you will see a lot of the photos and posters used to promote the movie. The stage play poster should not have the look or sentiment of the movie poster in any way.

```html
<!DOCTYPE html>
<html lang="en">
<head>
<meta charset="utf-8">
<title>Meet Me at the Corner Drugstore, Rusty Calhoun, Rusty Calhoun — Poster</title>
<link href="https://fonts.googleapis.com/css2?family=Sancreek&family=Lobster&family=Rye&display=swap" rel="stylesheet">
<style>
  :root {
    --sky-top: #d9502b;
    --sky-mid: #e8722f;
    --sky-low: #ec8a3e;
    --band: #f4a25a;
    --sun: #f9c24e;
    --sun-band: #fbd27a;
    --title-red: #e3262f;
    --title-shadow: #8e1418;
    --script-teal: #2fa7a8;
    --script-shadow: #5a2a18;
    --ground: #1b1a19;
    --silhouette-soft: rgba(30, 28, 27, 0.18);
    --silhouette-deep: rgba(30, 28, 27, 0.78);
    --credit-yellow: #f6c552;
  }
  * { margin: 0; padding: 0; box-sizing: border-box; }
  html, body { width: 848px; height: 1200px; overflow: hidden; background: var(--ground); }
  .poster {
    position: relative;
    width: 848px;
    height: 1200px;
    overflow: hidden;
    background: linear-gradient(180deg, var(--sky-top) 0%, var(--sky-mid) 45%, var(--sky-low) 70%, var(--sky-mid) 88%);
  }
  .sky { position: absolute; inset: 0; }

  .title {
    position: absolute;
    left: 262px;
    top: 40px;
    width: 540px;
    text-align: center;
    font-family: "Sancreek", serif;
    font-weight: 400;
    color: var(--title-red);
    text-transform: uppercase;
    line-height: 1;
    text-shadow: 3px 3px 0 var(--title-shadow);
  }
  .title-line { display: flex; justify-content: center; align-items: center; gap: 8px; }
  .title-big { font-size: 104px; letter-spacing: 1px; }
  .title-mid { font-size: 80px; margin-top: 4px; }
  .title-stack { display: flex; flex-direction: column; font-size: 38px; line-height: 0.95; }
  .title-rule { display: block; height: 6px; margin: 8px 14px 0; background: var(--title-red); box-shadow: 3px 3px 0 var(--title-shadow); }

  .subtitle {
    position: absolute;
    left: 252px;
    top: 345px;
    width: 560px;
    font-family: "Lobster", cursive;
    font-size: 60px;
    line-height: 1.05;
    color: var(--script-teal);
    text-shadow: 2px 3px 0 var(--script-shadow);
  }
  .subtitle-line { display: block; }
  .subtitle-line--second { padding-left: 150px; }

  .playwright {
    position: absolute;
    left: 262px;
    top: 522px;
    width: 540px;
    text-align: center;
    font-family: "Sancreek", serif;
    font-size: 58px;
    color: var(--title-red);
    text-transform: uppercase;
    text-shadow: 2px 2px 0 var(--title-shadow);
  }
  .playwright-by { font-size: 40px; }

  .figure, .pump, .derrick {
    position: absolute;
    background: linear-gradient(180deg, var(--silhouette-soft) 0%, var(--silhouette-deep) 100%);
    border-radius: 40px 40px 0 0;
  }
  .figure  { left: 70px;  top: 470px; width: 180px; height: 577px; }
  .pump    { left: 360px; top: 760px; width: 290px; height: 287px; }
  .derrick { left: 705px; top: 620px; width: 100px; height: 427px; }

  .ground {
    position: absolute;
    left: 0; bottom: 0;
    width: 848px; height: 153px;
    background: var(--ground);
  }
  .director {
    position: absolute;
    left: 0; top: 1112px;
    width: 848px;
    text-align: center;
    font-family: "Rye", serif;
    color: var(--credit-yellow);
    text-transform: uppercase;
    font-size: 34px;
    letter-spacing: 1px;
  }
  .director-label { font-size: 22px; letter-spacing: 3px; margin-right: 6px; }
</style>
</head>
<body>
<main class="poster">
  <svg class="sky" width="848" height="1200" viewBox="0 0 848 1200" aria-hidden="true">
    <g fill="var(--band)" opacity="0.55">
      <rect x="-40" y="160" width="420" height="34" rx="17"/>
      <rect x="-60" y="560" width="760" height="40" rx="20"/>
      <rect x="300" y="640" width="640" height="34" rx="17"/>
      <rect x="-40" y="720" width="520" height="46" rx="23"/>
      <rect x="420" y="800" width="520" height="30" rx="15"/>
      <rect x="-40" y="880" width="700" height="40" rx="20"/>
    </g>
    <circle cx="510" cy="262" r="408" fill="var(--sun)"/>
    <g fill="var(--sun-band)" opacity="0.7">
      <rect x="100" y="190" width="330" height="26" rx="13"/>
      <rect x="560" y="420" width="340" height="26" rx="13"/>
      <rect x="180" y="560" width="420" height="22" rx="11"/>
    </g>
  </svg>

  <h1 class="title">
    <span class="title-line">
      <span class="title-big">Meet Me</span>
      <span class="title-stack"><span>At</span><span>The</span></span>
    </span>
    <span class="title-line title-mid">Corner Drugstore</span>
    <span class="title-rule"></span>
  </h1>

  <p class="subtitle">
    <span class="subtitle-line">Rusty Calhoun,</span>
    <span class="subtitle-line subtitle-line--second">Rusty Calhoun</span>
  </p>

  <p class="playwright"><span class="playwright-by">By</span> Al Moravec</p>

  <div class="figure" role="img" aria-label="Silhouette of a man in a cowboy hat gazing toward the horizon"></div>
  <div class="pump" role="img" aria-label="Silhouette of an oil pumpjack"></div>
  <div class="derrick" role="img" aria-label="Silhouette of an oil derrick tower"></div>

  <div class="ground"></div>
  <p class="director"><span class="director-label">Directed by</span> Roy Pettibone</p>
</main>
</body>
</html>
```